A wine Label for a new brand of New Zealand Wine

We are looking for a Wine Label for our "Harbor Crest" brand of wines from North Otago New Zealand. We would like the label to perhaps use the HC as a logo and the rest up to the designer. We have our vineyards located in the Waitaki Valley New Zealand which is a southern region with mountains and a river flowing past our vineyard. Photos attached of Dramatic Landscape. Also attached is a basic outline of requirements for the front bottle of the label. The rear bottle label will contain writing about the wines background plus statutory regulations on Alc. Vol, bar code etc. Front Label size to be no Larger than 80mm deep by 100 mm wide. The label can be simple or graphic, whatever the designer chooses.
Target Market(s)
New Wine Brand
Look and feel
Each slider illustrates characteristics of the customer's brand and the style your logo design should communicate.

```html
<!DOCTYPE html>
<html lang="en">
<head>
<meta charset="utf-8">
<title>Harbor Crest – Pinot Gris Front Label</title>
<link rel="stylesheet" href="https://fonts.googleapis.com/css2?family=Marcellus&family=Playfair+Display:ital@1&family=Tinos&display=swap">
<style>
  :root {
    --page: #e6e6e6;
    --label-black: #0b0a09;
    --frame-gold: #c9a45f;
    --type-gold: #a47c46;
    --vintage-red: #9a3d1e;
    --hill-light: #a8834f;
    --hill-mid: #86663b;
    --hill-dark: #4a3720;
  }
  * { box-sizing: border-box; margin: 0; padding: 0; }
  html, body {
    width: 998px;
    height: 1200px;
    overflow: hidden;
    background: var(--page);
  }
  .wine-label {
    position: absolute;
    left: 189px;
    top: 95px;
    width: 620px;
    height: 1010px;
    background: var(--label-black);
  }
  .label-frame {
    position: absolute;
    inset: 15px;
    border: 3px solid var(--frame-gold);
  }
  .monogram {
    position: absolute;
    top: 92px;
    left: 0;
    right: 0;
    display: flex;
    justify-content: center;
    align-items: center;
    gap: 14px;
    font-family: "Marcellus", serif;
    font-size: 44px;
    color: var(--type-gold);
    line-height: 1;
  }
  .monogram-square {
    width: 26px;
    height: 26px;
    border: 2px solid var(--type-gold);
  }
  .brand-name {
    position: absolute;
    top: 196px;
    left: 0;
    right: 0;
    text-align: center;
    font-family: "Marcellus", serif;
    font-weight: 400;
    font-size: 76px;
    line-height: 1;
    color: var(--type-gold);
  }
  .landscape {
    position: absolute;
    top: 330px;
    left: 69px;
    width: 482px;
    height: 300px;
    background: linear-gradient(180deg,
      rgba(168, 131, 79, 0) 0%,
      var(--hill-light) 22%,
      var(--hill-mid) 55%,
      var(--hill-dark) 85%,
      rgba(74, 55, 32, 0) 100%);
    -webkit-mask-image: linear-gradient(90deg, transparent 0%, #000 8%, #000 92%, transparent 100%);
    mask-image: linear-gradient(90deg, transparent 0%, #000 8%, #000 92%, transparent 100%);
  }
  .varietal {
    position: absolute;
    top: 646px;
    left: 0;
    right: 0;
    text-align: center;
    font-family: "Marcellus", serif;
    font-weight: 400;
    font-size: 72px;
    line-height: 1;
    color: var(--type-gold);
    letter-spacing: 1px;
  }
  .varietal-rule {
    position: absolute;
    top: 736px;
    left: 73px;
    right: 73px;
    height: 2px;
    background: var(--type-gold);
  }
  .vintage {
    position: absolute;
    top: 760px;
    left: 0;
    right: 0;
    text-align: center;
    font-family: "Marcellus", serif;
    font-size: 38px;
    line-height: 1;
    color: var(--vintage-red);
  }
  .region {
    position: absolute;
    top: 840px;
    left: 0;
    right: 0;
    text-align: center;
    font-family: "Playfair Display", serif;
    font-style: italic;
    font-size: 26px;
    color: var(--type-gold);
  }
  .origin {
    position: absolute;
    top: 884px;
    left: 0;
    right: 0;
    text-align: center;
    font-family: "Tinos", serif;
    font-size: 24px;
    color: var(--type-gold);
  }
</style>
</head>
<body>
  <section class="wine-label">
    <div class="label-frame"></div>
    <div class="monogram"><span class="monogram-square"></span><span>HC</span></div>
    <h1 class="brand-name">Harbor Crest</h1>
    <div class="landscape" role="img" aria-label="Gold engraved landscape of the Waitaki Valley mountains, river and vineyard"></div>
    <h2 class="varietal">PINOT GRIS</h2>
    <div class="varietal-rule"></div>
    <p class="vintage">2015</p>
    <p class="region">Waitaki Valley ~ North Otago</p>
    <p class="origin">New Zealand Wine</p>
  </section>
</body>
</html>
```